Virtual assistant company needs letterhead and email signature

We need a letterhead and email signature for our virtual assistant company - dayBramble (small w capital F). Our tag line is think ahead | dayBramble

The colours we would like used are;

#81788c
#dddbe1

For reference our business cards have used #81788c background colour and #dddbe1 text

The fonts we would like used are

Lora
Proxima Nova

Please check out our twitter and facebook for style and feel

Twitter: @daybramble
www.chatterlane.com/daybramble

Please also find attached our landing page and business cards for reference

Any questions please let us know

Thanks
E

Reason: We like the opportunity to receive furthur designs

```html
<!DOCTYPE html>
<html lang="en">
<head>
<meta charset="utf-8">
<title>dayBramble — Email Signature</title>
<link rel="stylesheet" href="https://fonts.googleapis.com/css2?family=Lora:wght@400&family=Open+Sans:wght@300;400&display=swap">
<style>
  :root {
    --brand-plum: #81788c;
    --brand-plum-deep: #736a7f;
    --brand-mist: #dddbe1;
    --page-bg: #ffffff;
  }
  * { margin: 0; padding: 0; box-sizing: border-box; }
  html, body {
    width: 1200px;
    height: 1000px;
    overflow: hidden;
    background: var(--page-bg);
  }
  .canvas {
    position: relative;
    width: 1200px;
    height: 1000px;
    display: flex;
    align-items: center;
    justify-content: center;
  }
  .signature {
    position: relative;
    width: 960px;
    height: 240px;
    background: var(--brand-plum);
    overflow: hidden;
    color: var(--brand-mist);
  }
  .signature__sketch {
    position: absolute;
    inset: 0;
    background: linear-gradient(180deg, rgba(221,219,225,0.22) 0%, rgba(221,219,225,0.08) 45%, rgba(129,120,140,0) 75%);
  }
  .signature__brand {
    position: absolute;
    left: 34px;
    top: 112px;
  }
  .signature__name {
    font-family: "Lora", Georgia, serif;
    font-weight: 400;
    font-size: 82px;
    line-height: 1;
    letter-spacing: 0.5px;
    color: var(--brand-mist);
  }
  .signature__tagline {
    margin-top: 8px;
    margin-left: 62px;
    font-family: "Open Sans", Arial, sans-serif;
    font-weight: 400;
    font-size: 24px;
    letter-spacing: 0.5px;
    color: var(--brand-mist);
    white-space: pre;
  }
  .signature__contacts {
    position: absolute;
    left: 620px;
    top: 136px;
    list-style: none;
  }
  .contact {
    display: flex;
    align-items: center;
    height: 31px;
    font-family: "Open Sans", Arial, sans-serif;
    font-weight: 300;
    font-size: 25px;
    color: var(--brand-mist);
    letter-spacing: 0.3px;
  }
  .contact__icon {
    width: 20px;
    height: 20px;
    margin-right: 12px;
    flex: none;
  }
</style>
</head>
<body>
  <main class="canvas">
    <section class="signature" aria-label="dayBramble email signature">
      <div class="signature__sketch" role="img" aria-label="Faint hand-drawn planning sketches: concept notes, arrows, charts and diagrams"></div>

      <div class="signature__brand">
        <div class="signature__name">dayBramble</div>
        <div class="signature__tagline">think ahead  |  dayBramble</div>
      </div>

      <ul class="signature__contacts">
        <li class="contact">
          <svg class="contact__icon" viewBox="0 0 20 20" aria-hidden="true">
            <path d="M5 2 L8 5.5 L6.2 7.5 C7.2 9.8 9.8 12.6 12.3 13.8 L14.4 11.9 L18 15 L16 18 C9.5 18 2 10.5 2 4 Z" fill="var(--brand-mist)"/>
          </svg>
          <span>+ 55 11 4170 2289</span>
        </li>
        <li class="contact">
          <svg class="contact__icon" viewBox="0 0 20 20" aria-hidden="true">
            <rect x="2" y="5" width="16" height="11" fill="var(--brand-mist)"/>
            <path d="M2.5 5.5 L10 11 L17.5 5.5" fill="none" stroke="var(--brand-plum)" stroke-width="1.4"/>
          </svg>
          <span>info@daybramble.com</span>
        </li>
        <li class="contact">
          <svg class="contact__icon" viewBox="0 0 20 20" aria-hidden="true">
            <circle cx="10" cy="10" r="8" fill="var(--brand-mist)"/>
            <ellipse cx="10" cy="10" rx="3.5" ry="8" fill="none" stroke="var(--brand-plum)" stroke-width="1.2"/>
            <line x1="2" y1="10" x2="18" y2="10" stroke="var(--brand-plum)" stroke-width="1.2"/>
          </svg>
          <span>www.daybramble.com</span>
        </li>
      </ul>
    </section>
  </main>
</body>
</html>
```